Design some Business Cards for Varnholt Networks, Inc.

Using the existing logo, please design business cards for Varnholt Networks, Inc.

Varnholt Networks, Inc. is a Internet Telephony Service provider, providing hosted services, including, but not limited to, PBX, ACD, Desktop, Email, Applications, etc.

```html
<!DOCTYPE html>
<html lang="en">
<head>
<meta charset="utf-8">
<title>Varnholt Networks, Inc. – Business Cards</title>
<link href="https://fonts.googleapis.com/css2?family=Questrial&display=swap" rel="stylesheet">
<style>
  :root {
    --stage: #e9e9e9;
    --card-black: #0b0b0c;
    --card-sheen: #3a3b3e;
    --brand-white: #f2f2f2;
    --brand-blue: #35c3f0;
    --brand-amber: #fbb947;
    --ink-dark: #4a3410;
  }
  * { margin: 0; padding: 0; box-sizing: border-box; }
  html, body { width: 1200px; height: 645px; overflow: hidden; }
  body {
    background: var(--stage);
    font-family: "Questrial", "Century Gothic", sans-serif;
    display: flex;
    align-items: center;
    justify-content: center;
    gap: 60px;
  }
  .card {
    position: relative;
    width: 530px;
    height: 303px;
    overflow: hidden;
    background: radial-gradient(ellipse at 45% 20%, var(--card-sheen) 0%, var(--card-black) 60%);
    box-shadow: 0 8px 22px rgba(0,0,0,.25);
  }
  .brand {
    position: absolute;
    display: flex;
    align-items: center;
    color: var(--brand-white);
    text-transform: uppercase;
    letter-spacing: .04em;
    white-space: nowrap;
  }
  .brand-mark {
    border-radius: 50%;
    background: var(--brand-blue);
    flex: none;
  }
  /* front */
  .card-front .brand { left: 50%; top: 50%; transform: translate(-50%, -50%); gap: 18px; font-size: 38px; }
  .card-front .brand-mark { width: 70px; height: 70px; }
  /* back */
  .card-back .brand { left: 30px; top: 34px; gap: 12px; font-size: 25px; }
  .card-back .brand-mark { width: 46px; height: 46px; }
  .name-band {
    position: absolute;
    left: 50%; right: 0; top: 100px; height: 52px;
    background: var(--brand-amber);
    padding: 9px 0 0 26px;
    color: var(--ink-dark);
  }
  .person-name { font-size: 17px; letter-spacing: .05em; text-transform: uppercase; }
  .person-title { font-size: 9px; letter-spacing: .12em; text-transform: uppercase; margin-top: 3px; }
  .contact-band {
    position: absolute;
    left: 0; width: 42%; top: 178px; height: 74px;
    background: var(--brand-blue);
  }
  .contact-list {
    position: absolute;
    left: 47%; top: 184px;
    list-style: none;
    color: var(--brand-white);
    font-size: 12px;
    line-height: 1.65;
  }
</style>
</head>
<body>
  <section class="card card-front" aria-label="Business card front">
    <div class="brand"><span class="brand-mark"></span>Varnholt Networks</div>
  </section>

  <section class="card card-back" aria-label="Business card back">
    <div class="brand"><span class="brand-mark"></span>Varnholt Networks</div>
    <div class="name-band">
      <p class="person-name">Dalen Morrow</p>
      <p class="person-title">Director</p>
    </div>
    <div class="contact-band"></div>
    <ul class="contact-list">
      <li>(555) 014-2290</li>
      <li>www.varnholtnet.com</li>
      <li>helpdesk@varnholtnet.com</li>
    </ul>
  </section>
</body>
</html>
```